IT business looking for Standout Letterhead Design

We need a letterhead design for a company based in San Diego, CA called Corvane Systems, Inc. We specialize in IT engineering, installation and technical support pertaining to the department of defense.

We would like to see a design that incorporates the black and gold that matches our company logo.

More information on the company can be found at www.corvane-sys.example

```html
<!DOCTYPE html>
<html lang="en">
<head>
<meta charset="utf-8">
<title>Corvane Systems, Inc. — Letterhead</title>
<link rel="stylesheet" href="https://fonts.googleapis.com/css2?family=Open+Sans:wght@700&family=Libre+Baskerville:wght@400;700&family=Cinzel:wght@400&display=swap">
<style>
  :root {
    --gold: #a89513;
    --gold-bright: #b9a51c;
    --ink: #231f1e;
    --paper: #ffffff;
    --rule: #222222;
    --mark-faint: #ebe9e4;
  }
  html, body {
    margin: 0;
    padding: 0;
    overflow: hidden;
    background: var(--paper);
  }
  .letterhead {
    position: relative;
    width: 841px;
    height: 1200px;
    background: var(--paper);
    overflow: hidden;
    font-family: "Libre Baskerville", Georgia, serif;
    color: var(--ink);
  }
  .masthead-shapes {
    position: absolute;
    top: 0;
    left: 0;
    display: block;
  }
  .brand {
    position: absolute;
    left: 8px;
    top: 6px;
    width: 150px;
    display: flex;
    flex-direction: column;
    align-items: center;
  }
  .brand-dot {
    width: 14px;
    height: 14px;
    border-radius: 50%;
    background: var(--ink);
    margin-bottom: 4px;
  }
  .brand-name {
    font-family: "Cinzel", Georgia, serif;
    font-size: 15px;
    line-height: 1;
    color: var(--ink);
    letter-spacing: 0.5px;
  }
  .brand-sub {
    font-family: "Cinzel", Georgia, serif;
    font-size: 5px;
    color: var(--ink);
    margin-top: 3px;
    letter-spacing: 0.5px;
  }
  .company-title {
    position: absolute;
    left: 250px;
    width: 420px;
    top: 6px;
    margin: 0;
    text-align: center;
    font-family: "Open Sans", Arial, sans-serif;
    font-weight: 700;
    font-size: 24px;
    color: var(--gold-bright);
    line-height: 1.2;
  }
  .tagline {
    position: absolute;
    top: 61px;
    left: 0;
    width: 841px;
    height: 16px;
    margin: 0;
    text-align: center;
    font-family: "Open Sans", Arial, sans-serif;
    font-weight: 700;
    font-size: 12px;
    line-height: 16px;
    color: var(--gold-bright);
  }
  .fields {
    position: absolute;
    top: 106px;
    left: 21px;
    right: 32px;
    display: flex;
    justify-content: space-between;
    font-size: 14px;
  }
  .field {
    display: flex;
    align-items: flex-end;
    gap: 6px;
  }
  .field-line {
    display: inline-block;
    width: 84px;
    border-bottom: 1px solid var(--rule);
    margin-bottom: 3px;
  }
  .field-ref .field-line { width: 84px; margin-left: -4px; }
  .faint-mark {
    position: absolute;
    top: 560px;
    left: 0;
    width: 841px;
    text-align: center;
    font-family: "Cinzel", Georgia, serif;
    font-size: 96px;
    color: var(--mark-faint);
    letter-spacing: 4px;
  }
  .footer {
    position: absolute;
    left: 0;
    bottom: 0;
    width: 841px;
    text-align: center;
    font-weight: 700;
    font-size: 14px;
  }
  .footer-band {
    background: var(--gold);
    color: var(--ink);
    height: 19px;
    line-height: 19px;
  }
  .footer-contact {
    background: var(--ink);
    color: var(--gold-bright);
    height: 39px;
    padding-top: 1px;
    box-sizing: border-box;
    line-height: 18px;
  }
  .footer p { margin: 0; }
</style>
</head>
<body>
  <div class="letterhead">
    <svg class="masthead-shapes" width="841" height="78" viewBox="0 0 841 78" aria-hidden="true">
      <rect x="0" y="0" width="841" height="45" fill="var(--ink)"/>
      <polygon points="0,0 180,0 252,45 0,45" fill="var(--gold)"/>
      <rect x="0" y="45" width="841" height="16" fill="var(--gold)"/>
      <rect x="0" y="61" width="841" height="17" fill="var(--ink)"/>
    </svg>

    <div class="brand">
      <span class="brand-dot"></span>
      <span class="brand-name">CORVANE</span>
      <span class="brand-sub">SYSTEMS INC</span>
    </div>

    <h1 class="company-title">Corvane Systems Inc.</h1>
    <p class="tagline">Deals in IT Engineering, Installation &amp; Technical Support</p>

    <div class="fields">
      <div class="field field-date"><span>Date:</span><span class="field-line"></span></div>
      <div class="field field-ref"><span>Reference #:</span><span class="field-line"></span></div>
    </div>

    <div class="faint-mark" aria-hidden="true">CORVANE</div>

    <footer class="footer">
      <div class="footer-band"><p>Corvane Systems, Incorporation, San Diego, CA</p></div>
      <div class="footer-contact">
        <p>Phone: 619-555-0142, Facsimile: 619-555-0187</p>
        <p>www.corvane-sys.example, e-mail: info@corvane-sys.example</p>
      </div>
    </footer>
  </div>
</body>
</html>
```